A modern web page for a software product

We need a web page for a software product, which is an advanced solution based on Machine Learning and Natural Language processing. We already have a logo of the product and expect the web page to be inline with the logo colors. The design should be for one page web site with scrolled sections - details of the content and guidelines in the attachments.

Target Market(s)

software company

Industry/Entity Type

It Company

Number of Pages Required

1 page

Colors

Designer to choose colors to be used in the design.

Requirements
Must have
• - modern icons and graphics
• - inline with the logo colors
• - be related to Machine Learining, AI, data processing
• - should have two language versions: english and polish both are attached.
Nice to have
• - animation/motion
Should not have
• - any photos embedded

```html
<!DOCTYPE html>
<html lang="en">
<head>
<meta charset="utf-8">
<title>Veridata – Discovery and Classification of Personal Data</title>
<link href="https://fonts.googleapis.com/css2?family=Lato:wght@300;400;700&display=swap" rel="stylesheet">
<style>
:root{
  --teal:#17b3ad;
  --teal-dark:#0f9c97;
  --navy:#1d3c78;
  --ink:#1f3552;
  --text:#444b55;
  --muted:#8a8f96;
  --line:#c9ccd1;
  --grey-band:#e5e5e6;
  --white:#ffffff;
}
*{box-sizing:border-box;margin:0;padding:0}
html,body{width:1200px;height:3141px;overflow:hidden}
body{font-family:'Lato',sans-serif;color:var(--text);background:var(--white);position:relative}
svg{display:block}

/* header */
.site-header{position:absolute;top:0;left:0;width:1200px;height:88px;background:var(--white)}
.brand{position:absolute;left:125px;top:26px;display:flex;align-items:center;gap:10px;font-size:30px;font-weight:700;color:var(--navy)}
.brand-dot{width:22px;height:22px;background:var(--teal);border-radius:50%}
.main-nav{position:absolute;top:34px;left:331px}
.main-nav a{font-size:16px;color:#2b2f36;text-decoration:none;position:absolute;white-space:nowrap}
.main-nav a.active{color:var(--teal)}
.lang{position:absolute;left:915px;top:32px;font-size:13px;color:var(--muted);letter-spacing:.3px}
.flag{position:absolute;top:32px;width:30px;height:18px}
.flag-en{left:999px;background:#2a3f86}
.flag-pl{left:1045px;background:linear-gradient(#fff 0 50%,#d62b3a 50% 100%);border:1px solid #ddd}

/* hero */
.hero{position:absolute;top:88px;left:0;width:1200px;height:565px;
  background:radial-gradient(ellipse at 75% 40%,rgba(170,185,205,.55),transparent 55%),
  linear-gradient(160deg,#4a5a78 0%,#2c3b58 45%,#5b6a84 75%,#3a4863 100%)}
.hero-title{position:absolute;top:196px;left:0;width:1200px;text-align:center;color:var(--white);font-size:40px;font-weight:700;line-height:46px;letter-spacing:.5px}
.hero-arrow{position:absolute;top:236px}

/* section headings */
.section-title{position:absolute;left:0;width:1200px;text-align:center;font-size:29px;font-weight:400;letter-spacing:.5px}

/* features */
.feature-main{position:absolute;left:117px;top:754px;width:963px;height:283px;border:1.5px solid var(--line)}
.feature-main .diagram{position:absolute;left:60px;top:36px;width:190px;height:210px;border-radius:6px;
  background:linear-gradient(180deg,#dfe6f0 0%,#d3ecec 100%)}
.num{color:var(--teal);font-weight:300}
.feature-main .num{position:absolute;left:310px;top:42px;font-size:66px;line-height:66px}
.feature-main h3{position:absolute;left:362px;top:50px;font-size:23px;font-weight:400;color:var(--ink);line-height:32px}
.feature-main ul{position:absolute;left:362px;top:132px;list-style:none;font-size:13.5px;line-height:27px;color:#5a6069}
.feature-card{position:absolute;width:312px;height:218px;border:1.5px solid var(--line)}
.feature-card .icon{position:absolute;left:40px;top:38px}
.feature-card .num{position:absolute;left:30px;top:118px;font-size:46px;line-height:48px}
.feature-card p{position:absolute;left:72px;top:128px;width:225px;font-size:15px;line-height:20px;color:#3b4048}

/* use cases */
.use-cases{position:absolute;top:1543px;left:0;width:1200px;height:446px;background:var(--teal)}
.use-cases .section-title{top:44px;color:var(--white)}
.case{position:absolute;display:flex;align-items:center;gap:14px;color:var(--white);font-size:14px;font-weight:700;line-height:19px}
.case .ring{width:60px;height:60px;border:2px solid var(--white);border-radius:50%;display:flex;align-items:center;justify-content:center;flex:none}

/* highlights */
.highlights{position:absolute;top:1989px;left:0;width:1200px;height:649px;background:var(--grey-band)}
.highlights .section-title{top:42px;color:#222}
.hl-lead{position:absolute;left:207px;top:109px;width:794px;height:205px;background:var(--navy);color:var(--white)}
.hl-lead h3{position:absolute;left:90px;top:28px;font-size:20px;font-weight:700}
.hl-lead .tool{position:absolute;left:40px;top:24px}
.hl-lead ul{position:absolute;left:90px;top:70px;list-style:none;font-size:13.5px;line-height:27px}
.hl-lead li::before{content:"›";margin-right:12px;font-weight:700}
.hl-row{position:absolute;left:207px;width:799px;height:75px;background:var(--white);display:flex;align-items:center;gap:18px;padding-left:36px;font-size:18px;font-weight:700;color:var(--navy)}

/* contact */
.contact{position:absolute;top:2638px;left:0;width:1200px;height:415px;
  background:linear-gradient(100deg,#1d4f86 0%,#1d6f99 45%,#16a9ac 80%,#14b8ae 100%)}
.contact .section-title{top:77px;color:var(--white)}
.contact-line{position:absolute;left:0;width:1200px;display:flex;justify-content:center;align-items:center;gap:12px;color:var(--white);font-size:19px}
.socials{position:absolute;top:292px;left:0;width:1200px;display:flex;justify-content:center;gap:10px}
.socials span{width:46px;height:46px;border:2px solid var(--white);border-radius:50%;display:flex;align-items:center;justify-content:center}
.socials span i{width:12px;height:12px;background:var(--white);border-radius:50%}

/* footer */
.site-footer{position:absolute;top:3053px;left:0;width:1200px;height:88px;background:var(--white)}
.footer-nav{position:absolute;left:132px;top:35px;display:flex;gap:18px}
.footer-nav a{font-size:17px;color:#2b2f36;text-decoration:none}
.copyright{position:absolute;left:760px;top:36px;font-size:15px;color:var(--muted)}
</style>
</head>
<body>

<header class="site-header">
  <div class="brand"><span class="brand-dot"></span>Veridata</div>
  <nav class="main-nav">
    <a class="active" style="left:0">HOME</a>
    <a style="left:77px">FEATURES</a>
    <a style="left:184px">USE CASES</a>
    <a style="left:293px">HIGHLIGHTS</a>
    <a style="left:417px">CONTACT</a>
  </nav>
  <span class="lang">LANGUAGE</span>
  <span class="flag flag-en" role="img" aria-label="English"></span>
  <span class="flag flag-pl" role="img" aria-label="Polish"></span>
</header>

<section class="hero" role="img" aria-label="Hand touching a tablet over printed charts and data reports">
  <svg class="hero-arrow" style="left:100px" width="24" height="40" viewBox="0 0 24 40"><path d="M20 4 4 20l16 16" fill="none" stroke="#fff" stroke-width="4"/></svg>
  <svg class="hero-arrow" style="left:1072px" width="24" height="40" viewBox="0 0 24 40"><path d="M4 4l16 16L4 36" fill="none" stroke="#fff" stroke-width="4"/></svg>
  <h1 class="hero-title">DISCOVERY AND CLASSIFICATION<br>OF PERSONAL DATA</h1>
</section>

<h2 class="section-title" style="top:694px;color:var(--ink)">OUR FEATURES</h2>

<article class="feature-main">
  <div class="diagram" role="img" aria-label="Illustration of a central database server connected to several data sources"></div>
  <span class="num">1</span>
  <h3>Detection of Personal and Sensitive<br>data for GDPR compliance</h3>
  <ul>
    <li>In structural sources (e.g. SQL servers)</li>
    <li>In unstructured sources (e.g.: documents, e-mails, logs, data streams)</li>
    <li>In "noisy" content written in natural language (e.g.: containing errors or custom formats)</li>
    <li>Built in ML models and rules for personal data used in Poland</li>
  </ul>
</article>

<article class="feature-card" style="left:113px;top:1053px">
  <svg class="icon" width="70" height="70" viewBox="0 0 70 70"><path d="M60 6C42 8 30 20 24 34l12 12c14-6 26-18 28-36z" fill="#1d3c78"/><circle cx="46" cy="24" r="5" fill="#fff"/><path d="M24 34l-12 2-6 8 14 0zM36 46l-2 12-8 6 0-14z" fill="#17b3ad"/><path d="M18 50l-8 10" stroke="#17b3ad" stroke-width="3"/></svg>
  <span class="num">2</span><p>Fast Cataloging and Classification of data and sources</p>
</article>
<article class="feature-card" style="left:442px;top:1053px">
  <svg class="icon" width="80" height="76" viewBox="0 0 80 76" fill="none" stroke="#1d3c78" stroke-width="3"><path d="M4 4h34l10 10v54H4z"/><path d="M12 20h24M12 30h24M12 40h14"/><rect x="30" y="38" width="44" height="32" stroke="#17b3ad"/><path d="M30 48h44M30 59h44M45 38v32M60 38v32" stroke="#17b3ad"/></svg>
  <span class="num">3</span><p>Unified Data registry for RODO compliance fulfilment</p>
</article>
<article class="feature-card" style="left:768px;top:1053px">
  <svg class="icon" width="70" height="76" viewBox="0 0 70 76" fill="none" stroke="#1d3c78" stroke-width="3"><rect x="6" y="4" width="58" height="14" rx="3"/><rect x="6" y="22" width="58" height="14" rx="3"/><rect x="6" y="40" width="58" height="14" rx="3"/><path d="M35 54v12M10 70h50" stroke="#17b3ad"/></svg>
  <span class="num">4</span><p>Management of consents and data access policies</p>
</article>
<article class="feature-card" style="left:113px;top:1281px">
  <svg class="icon" width="80" height="70" viewBox="0 0 80 70" fill="none" stroke="#1d3c78" stroke-width="3"><path d="M6 64h70"/><rect x="10" y="44" width="8" height="18"/><rect x="26" y="36" width="8" height="26"/><rect x="42" y="40" width="8" height="22"/><rect x="58" y="28" width="8" height="34"/><path d="M12 30l18-12 16 8 24-20" stroke="#17b3ad"/><circle cx="12" cy="30" r="4" stroke="#17b3ad"/><circle cx="30" cy="18" r="4" stroke="#17b3ad"/><circle cx="46" cy="26" r="4" stroke="#17b3ad"/><circle cx="70" cy="6" r="4" stroke="#17b3ad"/></svg>
  <span class="num">5</span><p>Customizable Analytics and Reporting</p>
</article>
<article class="feature-card" style="left:442px;top:1281px">
  <svg class="icon" width="80" height="76" viewBox="0 0 80 76"><circle cx="24" cy="24" r="16" fill="#1d3c78"/><circle cx="24" cy="24" r="6" fill="#fff"/><g stroke="#1d3c78" stroke-width="6"><path d="M24 2v8M24 38v8M2 24h8M38 24h8"/></g><rect x="30" y="30" width="44" height="40" fill="#fff" stroke="#17b3ad" stroke-width="3"/><path d="M36 42l4 4 6-7M36 56l4 4 6-7M52 43h16M52 57h16" stroke="#17b3ad" stroke-width="3" fill="none"/></svg>
  <span class="num">6</span><p>Ability to integrates with tools for data anonymization or depersonalization</p>
</article>
<article class="feature-card" style="left:768px;top:1281px">
  <svg class="icon" width="80" height="76" viewBox="0 0 80 76" fill="none" stroke="#1d3c78" stroke-width="3"><rect x="6" y="22" width="68" height="44"/><path d="M30 72h20M40 66v6"/><path d="M28 52c-6 0-6-10 2-9 2-8 16-8 17 0 8-1 8 9 1 9z" stroke="#17b3ad"/><path d="M20 22V8M32 22V4M48 22V4M60 22V8" stroke="#17b3ad"/><circle cx="20" cy="6" r="2.5" stroke="#17b3ad"/><circle cx="60" cy="6" r="2.5" stroke="#17b3ad"/></svg>
  <span class="num">7</span><p>RESTful API for system management and integration</p>
</article>

<section class="use-cases">
  <h2 class="section-title">USE CASES</h2>
  <div class="case" style="left:165px;top:108px;width:470px">
    <span class="ring"><svg width="26" height="30" viewBox="0 0 26 30" fill="none" stroke="#fff" stroke-width="2.5"><path d="M3 3h14l6 6v18H3z"/><path d="M7 13h12M7 18h12M7 23h8"/></svg></span>
    <span>Internal audits and verification of the current status - in preparation for ensuring RODO compliance RODO</span>
  </div>
  <div class="case" style="left:165px;top:194px;width:470px">
    <span class="ring"><svg width="26" height="30" viewBox="0 0 26 30" fill="none" stroke="#fff" stroke-width="2.5"><ellipse cx="13" cy="12" rx="10" ry="4"/><path d="M3 12v12c0 5 20 5 20 0V12M3 18c0 5 20 5 20 0M13 1v7M9 4l4 4 4-4"/></svg></span>
    <span>Cataloging Sources that store sensitive data</span>
  </div>
  <div class="case" style="left:165px;top:280px;width:470px">
    <span class="ring"><svg width="28" height="28" viewBox="0 0 28 28" fill="none" stroke="#fff" stroke-width="2.5"><rect x="3" y="3" width="22" height="22"/><path d="M8 10h2M13 10h8M8 15h2M13 15h8M8 20h2M13 20h8"/></svg></span>
    <span>Keeping the registry of personal data in order to implement rights to information, forgetfulness, data transfer</span>
  </div>
  <div class="case" style="left:659px;top:108px;width:420px">
    <span class="ring"><svg width="28" height="26" viewBox="0 0 28 26" fill="none" stroke="#fff" stroke-width="2.5"><rect x="2" y="2" width="24" height="16"/><path d="M6 14l5-5 4 3 7-7M10 24h8M14 18v6"/></svg></span>
    <span>Continuous monitoring and classification of data</span>
  </div>
  <div class="case" style="left:659px;top:194px;width:420px">
    <span class="ring"><svg width="28" height="28" viewBox="0 0 28 28"><path d="M4 8h6a4 4 0 1 1 8 0h6v6a4 4 0 1 1 0 8v4H4v-6a4 4 0 1 0 0-8z" fill="#fff"/></svg></span>
    <span>Use collected the data to create additional business value</span>
  </div>
</section>

<section class="highlights">
  <h2 class="section-title">HIGHLIGHTS</h2>
  <div class="hl-lead">
    <svg class="tool" width="36" height="36" viewBox="0 0 36 36"><path d="M30 4a9 9 0 0 0-11 11L4 30l3 3 15-15A9 9 0 0 0 33 7l-5 5-4-1-1-4z" fill="#fff"/></svg>
    <h3>Built in Support for detection of Polish personal data</h3>
    <ul>
      <li>Sensitive data type (eg.:ID, name, address, etc.)</li>
      <li>Context of data occurrence</li>
      <li>Metadata describing the data source (e.g. system, table, author, etc.)</li>
      <li>Metadata describing the detection process</li>
    </ul>
  </div>
  <div class="hl-row" style="top:327px">
    <svg width="34" height="34" viewBox="0 0 34 34"><circle cx="17" cy="17" r="10" fill="#17b3ad"/><circle cx="17" cy="17" r="4" fill="#fff"/><g stroke="#17b3ad" stroke-width="6"><path d="M17 1v8M17 25v8M1 17h8M25 17h8M6 6l5 5M23 23l5 5M28 6l-5 5M6 28l5-5"/></g></svg>
    High effectiveness of personal data detection (also "noisy" data) by combining
  </div>
  <div class="hl-row" style="top:415px">
    <svg width="34" height="30" viewBox="0 0 34 30"><path d="M3 26A15 15 0 1 1 31 26z" fill="#17b3ad"/><path d="M17 24l7-11" stroke="#fff" stroke-width="3"/><circle cx="17" cy="24" r="3" fill="#fff"/></svg>
    Ready for High performance Processing
  </div>
  <div class="hl-row" style="top:501px">
    <svg width="36" height="30" viewBox="0 0 36 30" fill="#17b3ad"><rect x="13" y="2" width="10" height="8"/><rect x="2" y="20" width="10" height="8"/><rect x="13" y="20" width="10" height="8"/><rect x="24" y="20" width="10" height="8"/><path d="M17 10h2v4h12v6h-2v-4H19v4h-2v-4H7v4H5v-6h12z"/></svg>
    Supports Structured and Unstructured Data Source
  </div>
</section>

<section class="contact" role="img" aria-label="World map background in blue and teal tones">
  <h2 class="section-title">CONTACT</h2>
  <div class="contact-line" style="top:146px"><svg width="14" height="20" viewBox="0 0 14 20"><path d="M7 0a7 7 0 0 0-7 7c0 5 7 13 7 13s7-8 7-13a7 7 0 0 0-7-7z" fill="#fff"/><circle cx="7" cy="7" r="2.5" fill="#1d6f99"/></svg>42 Harbor Lane, Suite 7, Maple Falls 55012</div>
  <div class="contact-line" style="top:194px"><svg width="20" height="20" viewBox="0 0 20 20"><path d="M4 1l4 4-2 3c1 2 4 5 6 6l3-2 4 4-3 3C9 19 1 11 1 4z" fill="none" stroke="#fff" stroke-width="1.6"/></svg>555.014.3827</div>
  <div class="contact-line" style="top:240px"><svg width="22" height="16" viewBox="0 0 22 16" fill="none" stroke="#fff" stroke-width="1.6"><rect x="1" y="1" width="20" height="14"/><path d="M1 1l10 8 10-8"/></svg>hello@veridata.example</div>
  <div class="socials"><span><i></i></span><span><i></i></span><span><i></i></span><span><i></i></span></div>
</section>

<footer class="site-footer">
  <nav class="footer-nav"><a>Home</a><a>Features</a><a>Use Cases</a><a>Highlights</a><a>Contact</a></nav>
  <span class="copyright">© 2018 Veridata  All right reserved</span>
</footer>

</body>
</html>
```